Project QL quella lash

To create a stunning new business card design for "QuellaXLash" please note attached photo. Would like to see rose gold colours, black or white back ground

Target Market(s)

Women 18 to 60

Contact Information for Business Card

Modern elegant with light floral design in chrom or chrom accents

Font styles to use
Script

Requirements
Must have
• Dust rose, blush pink or rose gold colours
Nice to have
• Gold colouring or accents

```html
<!DOCTYPE html>
<html lang="en">
<head>
<meta charset="utf-8">
<title>QuellaXLash Business Card</title>
<link rel="stylesheet" href="https://fonts.googleapis.com/css2?family=Cinzel:wght@500&family=Cormorant+Garamond:wght@400;500&display=swap">
<style>
  :root {
    --backdrop: #1d1d20;
    --marble-light: #fdfdfd;
    --marble-mid: #eef0f1;
    --marble-vein: rgba(150, 158, 164, 0.28);
    --marble-vein-soft: rgba(170, 176, 182, 0.16);
    --ink: #2b2b2d;
    --ink-soft: #3d3d40;
    --blush: #d3a198;
    --blush-soft: #e8c6bf;
    --rule: #d9aaa1;
  }
  * { margin: 0; padding: 0; box-sizing: border-box; }
  html, body {
    width: 1200px;
    height: 800px;
    overflow: hidden;
    background: var(--backdrop);
  }
  .canvas {
    position: relative;
    width: 1200px;
    height: 800px;
  }
  .card {
    position: absolute;
    left: 400px;
    top: 50px;
    width: 400px;
    height: 700px;
    border-radius: 28px;
    overflow: hidden;
    color: var(--ink);
  }
  .card__marble {
    position: absolute;
    inset: 0;
    background:
      linear-gradient(118deg, transparent 18%, var(--marble-vein-soft) 18.6%, transparent 19.4%),
      linear-gradient(128deg, transparent 41%, var(--marble-vein) 41.4%, transparent 42%),
      linear-gradient(112deg, transparent 57%, var(--marble-vein-soft) 58%, transparent 59.5%),
      linear-gradient(134deg, transparent 73%, var(--marble-vein) 73.3%, transparent 74%),
      linear-gradient(121deg, transparent 86%, var(--marble-vein-soft) 86.8%, transparent 88%),
      radial-gradient(ellipse at 15% 85%, #e3e6e8 0%, transparent 45%),
      radial-gradient(ellipse at 70% 55%, #f1f2f3 0%, transparent 50%),
      linear-gradient(160deg, var(--marble-light) 0%, var(--marble-mid) 60%, var(--marble-light) 100%);
  }
  .floral {
    position: absolute;
    left: 165px;
    top: 40px;
    width: 210px;
    height: 250px;
    border-radius: 48% 52% 45% 55% / 55% 45% 58% 42%;
    background: radial-gradient(ellipse at 48% 45%, var(--blush) 0%, var(--blush-soft) 55%, rgba(232, 198, 191, 0) 75%);
    opacity: 0.9;
  }
  .brand {
    position: absolute;
    left: 40px;
    top: 250px;
    display: flex;
    align-items: center;
    gap: 12px;
  }
  .brand__name {
    font-family: "Cormorant Garamond", serif;
    font-weight: 400;
    font-size: 50px;
    color: var(--ink-soft);
    letter-spacing: 0.01em;
    line-height: 1;
  }
  .person {
    position: absolute;
    left: 40px;
    top: 335px;
  }
  .person__name {
    font-family: "Cinzel", serif;
    font-weight: 500;
    font-size: 25px;
    letter-spacing: 0.2em;
    line-height: 1.1;
  }
  .person__title {
    font-family: "Cinzel", serif;
    font-weight: 500;
    font-size: 13px;
    letter-spacing: 0.24em;
    margin-top: 6px;
    color: var(--ink-soft);
  }
  .address {
    position: absolute;
    left: 40px;
    top: 410px;
    font-family: "Cormorant Garamond", serif;
    font-weight: 500;
    font-size: 17px;
    line-height: 1.35;
    color: var(--ink-soft);
  }
  .contact {
    position: absolute;
    left: 40px;
    top: 490px;
    width: 300px;
    font-family: "Cormorant Garamond", serif;
    font-weight: 500;
    font-size: 18px;
    color: var(--ink-soft);
  }
  .contact__row {
    display: flex;
    align-items: center;
    gap: 10px;
    height: 30px;
  }
  .contact__rule {
    height: 1px;
    background: var(--rule);
    margin: 10px 0;
    width: 200px;
  }
  .contact__icon {
    width: 18px;
    height: 18px;
    flex: none;
  }
</style>
</head>
<body>
<main class="canvas">
  <section class="card" aria-label="QuellaXLash business card">
    <div class="card__marble" role="img" aria-label="White marble texture with soft grey veining"></div>
    <div class="floral" role="img" aria-label="Soft blush pink floral watercolour accent"></div>

    <div class="brand">
      <p class="brand__name">QuellaXLash</p>
    </div>

    <div class="person">
      <p class="person__name">MAREN HOLLOWAY</p>
      <p class="person__title">MANAGING DIRECTOR</p>
    </div>

    <p class="address">118 Larkspur Avenue, #4<br>Fairhaven, OR 97410</p>

    <div class="contact">
      <div class="contact__rule"></div>
      <div class="contact__row">
        <span>555.014.2290</span>
        <svg class="contact__icon" viewBox="0 0 18 18" aria-hidden="true">
          <circle cx="9" cy="9" r="9" fill="#2b2b2d"/>
          <path d="M6.2 4.6c.4-.3.9-.2 1.1.2l.8 1.5c.2.4.1.8-.2 1.1l-.6.5c.4 1 1.2 1.8 2.2 2.2l.5-.6c.3-.3.7-.4 1.1-.2l1.5.8c.4.2.5.7.2 1.1l-.6.8c-.4.5-1.1.7-1.7.4C8 11.5 6.5 10 5.6 7.5c-.2-.6 0-1.3.4-1.7z" fill="#f3dcd7"/>
        </svg>
      </div>
      <div class="contact__rule"></div>
      <div class="contact__row">
        <svg class="contact__icon" viewBox="0 0 18 18" aria-hidden="true">
          <circle cx="9" cy="9" r="9" fill="#2b2b2d"/>
          <rect x="4.5" y="6" width="9" height="6.5" rx="0.8" fill="none" stroke="#f3dcd7" stroke-width="1.1"/>
          <path d="M4.8 6.4 9 9.6l4.2-3.2" fill="none" stroke="#f3dcd7" stroke-width="1.1"/>
        </svg>
      </div>
      <div class="contact__row">
        <span>hello@quellalash.com</span>
      </div>
    </div>
  </section>
</main>
</body>
</html>
```